New modern website for Kerbline Groundworks

Hi we are an existing company that has a current website http://www.kerblinegroundworks.co.nz/ we are looking to get a new vibrant looking website designed to take us further and gain more customers. We are after a simple easy to use website that does not confuse but we want to make an impact and stand out from the rest

Target Market(s)

Homeowners And Commercial Businesses

Industry/Entity Type

It Company

Coding

Coded - Design and coding required

Number of Pages Required

2 page

```html
<!DOCTYPE html>
<html lang="en">
<head>
<meta charset="utf-8">
<title>Kerbline Groundworks</title>
<link rel="stylesheet" href="https://fonts.googleapis.com/css2?family=Lato:wght@300;400;700;900&family=Open+Sans:wght@400;600&display=swap">
<style>
:root{
  --yellow:#fde92b;
  --ink:#111111;
  --text:#333333;
  --muted:#555555;
  --white:#ffffff;
  --footer:#2b2b2b;
  --footer-bar:#1f1f1f;
  --footer-text:#9a9a9a;
  --line:#e2c400;
}
*{box-sizing:border-box;margin:0;padding:0}
html,body{width:1200px;height:2597px;overflow:hidden;background:var(--white)}
body{position:relative;font-family:"Open Sans",Arial,sans-serif;color:var(--text)}
.abs{position:absolute}
.heading{font-family:"Lato",Arial,sans-serif}

/* header */
.site-header{position:absolute;left:0;top:0;width:1200px;height:92px;background:var(--white)}
.brand{position:absolute;left:69px;top:28px;font-family:"Lato",sans-serif;font-weight:900;font-size:27px;color:var(--ink);letter-spacing:.5px;text-transform:uppercase}
.nav{position:absolute;top:46px;font-family:"Lato",sans-serif;font-weight:700;font-size:15px;color:#222;text-transform:uppercase}
.nav-active::after{content:"";position:absolute;left:-6px;right:-6px;top:42px;height:4px;background:var(--yellow)}
.phone{position:absolute;left:964px;top:40px;display:flex;align-items:center;gap:12px;font-family:"Lato",sans-serif;font-size:21px;color:#222}

/* hero */
.hero{position:absolute;left:0;top:92px;width:1200px;height:521px;background:linear-gradient(180deg,#4a4642 0%,#3a3631 45%,#24211f 100%)}
.hero-title{position:absolute;left:0;width:1200px;text-align:center;color:var(--white);font-family:"Lato",sans-serif}
.hero-title.one{top:150px;font-size:44px;font-weight:900}
.hero-title.two{top:222px;font-size:40px;font-weight:400}
.hero-rule{position:absolute;left:343px;width:473px;height:3px;background:var(--yellow)}

/* call band */
.call-band{position:absolute;left:0;top:613px;width:1200px;height:102px;background:var(--yellow)}
.call-text{position:absolute;left:73px;top:32px;font-family:"Lato",sans-serif;font-weight:900;font-size:30px;color:var(--ink)}
.call-button{position:absolute;left:912px;top:24px;width:222px;height:57px;border:3px solid var(--ink);display:flex;align-items:center;justify-content:center;font-family:"Lato",sans-serif;font-weight:900;font-size:19px;color:var(--ink)}

/* feature cards */
.card{position:absolute;top:783px;width:502px;height:249px;color:var(--white);text-align:center;font-family:"Lato",sans-serif}
.card.services{left:71px;background:linear-gradient(180deg,#3c3c3c,#2c2c2c)}
.card.projects{left:629px;background:linear-gradient(180deg,#4b5142,#35382f)}
.card-title{position:absolute;left:0;right:0;top:52px;font-size:40px;font-weight:900}
.card-sub{position:absolute;left:0;right:0;top:120px;font-size:19px;font-weight:700;text-transform:uppercase}
.card-link{position:absolute;left:50%;top:172px;transform:translateX(-50%);font-size:17px;font-weight:900;padding-bottom:8px;border-bottom:3px solid var(--yellow)}

/* trust */
.trust-title{position:absolute;left:0;width:1200px;top:1128px;text-align:center;font-family:"Lato",sans-serif;font-weight:900;font-size:26px;color:var(--ink)}
.trust-sub{position:absolute;left:0;width:1200px;top:1171px;text-align:center;font-size:13px;color:#666;text-transform:uppercase;letter-spacing:.5px}
.bracket{position:absolute;width:34px;height:20px;border-color:#c9ad1a;border-style:solid}
.bracket.tl{left:185px;top:1117px;border-width:3px 0 0 3px}
.bracket.br{left:988px;top:1152px;border-width:0 3px 3px 0}
.feature{position:absolute;top:1224px;width:300px;text-align:center}
.feature-badge{width:160px;height:160px;margin:0 auto;border-radius:50%;background:radial-gradient(circle,#1c1c1c 0 54%,var(--yellow) 55% 88%,#1c1c1c 89% 92%,var(--yellow) 93%)}
.feature-rule{width:140px;height:2px;background:var(--yellow);margin:35px auto 0}
.feature-title{margin-top:12px;font-family:"Lato",sans-serif;font-weight:900;font-size:22px;letter-spacing:1px;color:var(--ink);text-transform:uppercase}
.feature-text{margin:18px auto 0;width:270px;font-size:14px;line-height:21px;color:var(--muted)}

/* gallery */
.gallery{position:absolute;left:0;top:1680px;width:1200px;height:601px;background:var(--yellow)}
.gallery-title{position:absolute;left:0;width:1200px;top:66px;text-align:center;font-family:"Lato",sans-serif;font-weight:900;font-size:30px;color:var(--ink)}
.shot{position:absolute}
.zoom{position:absolute;left:50%;top:50%;width:56px;height:56px;margin:-28px 0 0 -28px;border-radius:50%;background:#8a8a8a}

/* footer */
.site-footer{position:absolute;left:0;top:2281px;width:1200px;height:278px;background:var(--footer);color:var(--footer-text)}
.foot-head{position:absolute;top:41px;font-family:"Lato",sans-serif;font-weight:900;font-size:15px;color:var(--white);letter-spacing:1px;text-transform:uppercase;padding-bottom:8px;border-bottom:2px solid var(--yellow)}
.foot-brand{position:absolute;left:99px;top:88px;font-family:"Lato",sans-serif;font-weight:900;font-size:22px;color:var(--white);text-transform:uppercase}
.foot-about{position:absolute;left:99px;top:141px;width:320px;font-size:12px;line-height:24px}
.socials{position:absolute;left:99px;top:222px;display:flex;gap:12px}
.socials span{width:10px;height:10px;border-radius:50%;background:#bdbdbd}
.foot-link{position:absolute;font-size:13px;color:#c8c8c8}
.foot-link::before{content:"›";margin-right:10px;color:#777}
.foot-contact{position:absolute;left:831px;display:flex;align-items:center;gap:16px;font-size:13px;color:var(--footer-text)}
.foot-contact svg{width:14px;height:14px;fill:#999}
.foot-bar{position:absolute;left:0;top:2559px;width:1200px;height:38px;background:var(--footer-bar);color:#bdbdbd;font-size:13px;text-align:center;line-height:38px}
</style>
</head>
<body>

<header class="site-header">
  <div class="brand">Kerbline Groundworks</div>
  <span class="nav nav-active" style="left:464px">Home</span>
  <span class="nav" style="left:539px">About</span>
  <span class="nav" style="left:618px">Services</span>
  <span class="nav" style="left:719px">Projects</span>
  <span class="nav" style="left:823px">Contact Us</span>
  <div class="phone">
    <svg width="24" height="24" viewBox="0 0 24 24" aria-hidden="true"><path d="M6.6 10.8a15.1 15.1 0 0 0 6.6 6.6l2.2-2.2c.3-.3.7-.4 1-.2 1.1.4 2.3.6 3.6.6.6 0 1 .4 1 1V20c0 .6-.4 1-1 1A17 17 0 0 1 3 4c0-.6.4-1 1-1h3.5c.6 0 1 .4 1 1 0 1.3.2 2.5.6 3.6.1.3 0 .7-.2 1z" fill="#f2c200"/></svg>
    <span>09 555 01 42</span>
  </div>
</header>

<section class="hero" role="img" aria-label="Road crew in high-visibility gear spreading fresh asphalt with rakes">
  <h1 class="hero-title one">Your one-stop specialist for driveway</h1>
  <div class="hero-rule" style="top:223px"></div>
  <p class="hero-title two">construction in Auckland</p>
  <div class="hero-rule" style="top:285px"></div>
</section>

<section class="call-band">
  <p class="call-text">Any Questions you would like to ask? Need to talk to us...</p>
  <div class="call-button">CONTACT US</div>
</section>

<article class="card services" role="img" aria-label="Darkened photo of an asphalt job site with work vehicle">
  <h2 class="card-title">Our Services</h2>
  <p class="card-sub">Complete asphalt services for your next</p>
  <span class="card-link">READ MORE</span>
</article>
<article class="card projects" role="img" aria-label="Darkened photo of a finished residential driveway with garden">
  <h2 class="card-title">Project</h2>
  <p class="card-sub">For residential driveways and commercial</p>
  <span class="card-link">READ MORE</span>
</article>

<div class="bracket tl"></div>
<h2 class="trust-title">The trusted name for all Concrete &amp; Asphalt Paving in Auckland</h2>
<p class="trust-sub">Years of experience</p>
<div class="bracket br"></div>

<div class="feature" style="left:80px">
  <div class="feature-badge" role="img" aria-label="Round yellow badge marking 70 years of experience"></div>
  <div class="feature-rule"></div>
  <h3 class="feature-title">Our Expertise</h3>
  <p class="feature-text">We have a reputation with clients in and around Auckland for achieving great results on time and within budget every time. We are proud to share our years of experience.</p>
</div>
<div class="feature" style="left:439px">
  <div class="feature-badge" role="img" aria-label="Round yellow icon of a house with a driveway"></div>
  <div class="feature-rule"></div>
  <h3 class="feature-title">Concreting &amp; Work</h3>
  <p class="feature-text">When it comes to all asphalt services, you can rest assured we will work around your schedule, requirements and budget. Servicing throughout Auckland, we specialise in.</p>
</div>
<div class="feature" style="left:815px">
  <div class="feature-badge" role="img" aria-label="Round yellow icon of a worker digging"></div>
  <div class="feature-rule"></div>
  <h3 class="feature-title">Additional Services</h3>
  <p class="feature-text">As part of our asphalt services, we are proud to offer a range of related services to our clients in the eastern suburbs and greater Auckland. Specialising in residential, commercial and industrial projects.</p>
</div>

<section class="gallery">
  <h2 class="gallery-title">For residential driveways and commercial paving in Auckland</h2>
  <div class="shot" style="left:74px;top:168px;width:168px;height:147px;background:linear-gradient(160deg,#8c8c86,#3a3a3a)" role="img" aria-label="Fresh asphalt path with traffic cones"></div>
  <div class="shot" style="left:74px;top:337px;width:168px;height:148px;background:linear-gradient(160deg,#7f8a70,#3d3d3b)" role="img" aria-label="Asphalt entry path beside a garden"></div>
  <div class="shot" style="left:263px;top:168px;width:327px;height:317px;background:linear-gradient(180deg,#4a4a48,#262626)" role="img" aria-label="Crew laying concrete on a commercial slab"><span class="zoom"></span></div>
  <div class="shot" style="left:608px;top:168px;width:317px;height:317px;background:linear-gradient(180deg,#b9c3cc 0%,#9a5a5a 45%,#6d6d6d 100%)" role="img" aria-label="Fleet of red trucks parked on a sealed yard"></div>
  <div class="shot" style="left:942px;top:168px;width:170px;height:147px;background:linear-gradient(160deg,#8a8a7e,#4a4a48)" role="img" aria-label="Sealed driveway along a fence"></div>
  <div class="shot" style="left:942px;top:337px;width:170px;height:148px;background:linear-gradient(160deg,#7a6a4a,#2e2e2e)" role="img" aria-label="Asphalt driveway beside a retaining wall"></div>
</section>

<footer class="site-footer">
  <h4 class="foot-head" style="left:99px">About Us</h4>
  <div class="foot-brand">Kerbline Groundworks</div>
  <p class="foot-about">Structure works as international construction services company and is a leading builder in diverse and numerous market segments.</p>
  <div class="socials"><span></span><span></span><span></span><span></span><span></span><span></span><span></span></div>

  <h4 class="foot-head" style="left:464px">Information</h4>
  <span class="foot-link" style="left:466px;top:97px">Home</span>
  <span class="foot-link" style="left:466px;top:128px">Projects</span>
  <span class="foot-link" style="left:466px;top:159px">Certifications</span>
  <span class="foot-link" style="left:466px;top:190px">Core Values</span>
  <span class="foot-link" style="left:466px;top:221px">Our Partners</span>
  <span class="foot-link" style="left:626px;top:97px">Company</span>
  <span class="foot-link" style="left:626px;top:128px">Contact</span>
  <span class="foot-link" style="left:626px;top:159px">Company History</span>
  <span class="foot-link" style="left:626px;top:190px">FAQ</span>
  <span class="foot-link" style="left:626px;top:221px">Our Team</span>

  <h4 class="foot-head" style="left:831px">Structure Office</h4>
  <div class="foot-contact" style="top:96px"><svg viewBox="0 0 24 24"><path d="M12 2a7 7 0 0 0-7 7c0 5 7 13 7 13s7-8 7-13a7 7 0 0 0-7-7zm0 9.5A2.5 2.5 0 1 1 12 6.5a2.5 2.5 0 0 1 0 5z"/></svg><span>22 Harbour Lane, Ellerslie, Auckland.</span></div>
  <div class="foot-contact" style="top:127px"><svg viewBox="0 0 24 24"><path d="M6.6 10.8a15.1 15.1 0 0 0 6.6 6.6l2.2-2.2c.3-.3.7-.4 1-.2 1.1.4 2.3.6 3.6.6.6 0 1 .4 1 1V20c0 .6-.4 1-1 1A17 17 0 0 1 3 4c0-.6.4-1 1-1h3.5c.6 0 1 .4 1 1 0 1.3.2 2.5.6 3.6.1.3 0 .7-.2 1z"/></svg><span>(09) 555 0100</span></div>
  <div class="foot-contact" style="top:158px"><svg viewBox="0 0 24 24"><path d="M2 5h20v14H2zm2 2v.5l8 5 8-5V7z"/></svg><span>hello@kerbline.co.nz</span></div>
  <div class="foot-contact" style="top:189px"><svg viewBox="0 0 24 24"><path d="M6 2h9l3 3v4h2a2 2 0 0 1 2 2v9H2v-9a2 2 0 0 1 2-2h2zm2 2v5h8V6h-2V4z"/></svg><span>(09) 555 0199</span></div>
  <div class="foot-contact" style="top:220px"><svg viewBox="0 0 24 24"><path d="M12 2a10 10 0 1 0 0 20 10 10 0 0 0 0-20zm1 10.4 4 2.3-1 1.7-5-3V6h2z"/></svg><span>Mon - Sat: 9:00 - 18:00</span></div>
</footer>
<div class="foot-bar">Copyright © 2016 Kerbline Groundworks - All Rights Reserved.</div>

</body>
</html>
```